Top of the line business card design needed for real estate brokerage

We currently have a business card with our logo but would like to have a revised version. We would love for you to implement your own design that will catch anyone's attention. The theme colors should be black, royal blue, gray/silver, and white.The contact information should be the same as the info on our current business card (picture attached). In the design that we pick, we will need to be able to edit the text so that we can customize the text content for each of our agents. Same goes for the professional picture. There should be an area on the card that each agent can have their professional portrait attached. Please include a version without the picture option as well for agents that do not wish to have a professional picture attached.
Business

```html
<!DOCTYPE html>
<html lang="en">
<head>
<meta charset="utf-8">
<title>Clearstone Realty Business Cards</title>
<link rel="stylesheet" href="https://fonts.googleapis.com/css2?family=Arimo:wght@400;700&family=Open+Sans:wght@400&display=swap">
<style>
  :root {
    --page-bg: #2b2b2b;
    --card-light: #ffffff;
    --card-shade: #e4e4e4;
    --royal-blue: #0b4aa8;
    --ink: #1c1c1c;
    --silver: #9a9a9a;
    --portrait-top: #d7d9dc;
    --portrait-bottom: #2a2a2a;
  }
  * { margin: 0; padding: 0; box-sizing: border-box; }
  html, body { width: 1200px; height: 965px; overflow: hidden; }
  body { background: var(--page-bg); position: relative; font-family: "Arimo", Arial, sans-serif; color: var(--ink); }

  .card {
    position: absolute; left: 246px; width: 710px; height: 402px;
    background: radial-gradient(ellipse at 50% 40%, var(--card-light) 30%, var(--card-shade) 100%);
    box-shadow: 0 4px 14px rgba(0,0,0,.6);
    overflow: hidden;
  }
  .card-front { top: 60px; }
  .card-back { top: 504px; }

  .brand {
    position: absolute; display: flex; align-items: center; gap: 10px;
    font-family: "Arimo", Arial, sans-serif; font-weight: 700; color: var(--royal-blue);
    font-size: 26px; white-space: nowrap;
  }
  .brand-mark { width: 22px; height: 22px; background: var(--royal-blue); flex: none; }
  .card-front .brand { left: 70px; top: 185px; }
  .card-back .brand { left: 50px; top: 150px; }

  .divider {
    position: absolute; left: 343px; top: 60px; width: 2px; height: 290px;
    background: linear-gradient(to bottom, transparent, #b9c3d3 20%, #b9c3d3 80%, transparent);
  }

  .agent { position: absolute; left: 374px; top: 86px; }
  .agent-name { font-size: 23px; font-weight: 400; color: var(--royal-blue); line-height: 1.1; }
  .agent-title { font-size: 16px; line-height: 1.3; }

  .contact-list { position: absolute; left: 374px; top: 154px; list-style: none; }
  .contact-list li { display: flex; align-items: center; height: 20.3px; font-size: 16px; }
  .contact-list svg { width: 16px; height: 16px; margin-right: 9px; fill: var(--royal-blue); flex: none; }

  .address { position: absolute; left: 374px; top: 282px; font-size: 16px; line-height: 21px; font-style: normal; }

  .services {
    position: absolute; left: 50px; top: 276px;
    font-family: "Open Sans", Arial, sans-serif; font-size: 15.5px; line-height: 21px; color: #222;
  }

  .portrait {
    position: absolute; left: 443px; top: 74px; width: 223px; height: 254px;
    background: linear-gradient(to bottom, var(--portrait-top) 0%, #bfc3c8 35%, var(--portrait-bottom) 60%);
  }

  .band { position: absolute; left: 0; top: 328px; width: 100%; height: 48px; background: var(--royal-blue); }
</style>
</head>
<body>

<section class="card card-front">
  <div class="brand"><span class="brand-mark"></span>Clearstone Realty</div>
  <div class="divider"></div>

  <div class="agent">
    <h1 class="agent-name">Marcus Bellamy</h1>
    <p class="agent-title">Broker</p>
  </div>

  <ul class="contact-list">
    <li><svg viewBox="0 0 16 16"><rect x="1" y="2" width="4" height="12" rx="1"/><rect x="6" y="3" width="9" height="10" rx="1"/><rect x="8" y="5" width="5" height="2" fill="#fff"/></svg>555-210-4830</li>
    <li><svg viewBox="0 0 16 16"><rect x="4" y="1" width="8" height="14" rx="1.5"/><rect x="5.5" y="3" width="5" height="8" fill="#fff"/></svg>555-210-4917</li>
    <li><svg viewBox="0 0 16 16"><rect x="4" y="1" width="8" height="5"/><rect x="1" y="6" width="14" height="8" rx="1"/><rect x="4" y="10" width="8" height="2" fill="#fff"/></svg>555-210-4462</li>
    <li><svg viewBox="0 0 16 16"><rect x="1" y="3" width="14" height="10"/><path d="M1 3l7 6 7-6" stroke="#fff" stroke-width="1.4" fill="none"/></svg>marcus@clearstonerealty.com</li>
    <li><svg viewBox="0 0 16 16"><circle cx="8" cy="8" r="7"/><g stroke="#fff" stroke-width="1" fill="none"><ellipse cx="8" cy="8" rx="3" ry="7"/><path d="M1 8h14M2.5 4.5h11M2.5 11.5h11"/></g></svg>www.clearstonerealty.com</li>
  </ul>

  <address class="address">2750 Harbor View Rd, Suite 310<br>Lakeview Shores, FL 30418</address>
</section>

<section class="card card-back">
  <div class="brand"><span class="brand-mark"></span>Clearstone Realty</div>
  <p class="services">Residential Real Estate | Commercial Real Estate<br>Property Management | Investments</p>
  <div class="portrait" role="img" aria-label="Agent's professional portrait in dark suit"></div>
  <div class="band"></div>
</section>

</body>
</html>
```